Advertising poster for podcast event

"The Lantern Table" is one of the most popular podcasts in Switzerland (https://listen.harbofeed.example/show/4kqpVXRT219LmNaw8BYdE5). It is hosted by the two radio DJs Lukas Brenner and Rafael Tanner. For a series of live shows where the podcast is recorded with an audience, we need a design of a poster. This should have the format A3 high. In addition, the image must be used that was uploaded here, because this is the cover photo with which you can always recognize the podcast. But what is designed around it is up to you. In addition, it must contain the following text:

- Title of the event:
The lantern table - Live
- Show dates:
Saturday, November 11, 2023 - Solothurn
Wednesday, December 27, 2023 - Berne
Thursday, December 28, 2023 - Berne
- A line with additional information about the presale:
The Dome, information and tickets: www.kuppelfest.example

Target Market(s)

Switzerland

Industry/Entity Type

Entertainment

Requirements
Must have
• The attached image and text according to the briefing.

```html
<!DOCTYPE html>
<html lang="en">
<head>
<meta charset="utf-8">
<title>The Lantern Table – Live</title>
<link rel="stylesheet" href="https://fonts.googleapis.com/css2?family=Saira+Condensed:wght@400;600;700&display=swap">
<style>
  :root {
    --mustard: #F2B01E;
    --ink: #231F20;
    --paper: #F7F3EC;
    --signal: #D42027;
    --dot-grey: #4A4A4D;
  }
  html, body {
    margin: 0;
    padding: 0;
    width: 849px;
    height: 1200px;
    overflow: hidden;
    background: var(--mustard);
  }
  .poster {
    display: block;
    width: 849px;
    height: 1200px;
    background: var(--mustard);
  }
  .mic-frame { fill: none; stroke: var(--ink); stroke-width: 30; stroke-linecap: round; }
  .mic-knob { fill: var(--ink); }
  .mic-cup { fill: var(--ink); }
  .mic-rim { fill: none; stroke: var(--mustard); stroke-width: 13; }
  .mic-band { fill: var(--ink); }
  .event-title {
    font-family: "Saira Condensed", sans-serif;
    font-weight: 700;
    font-size: 56px;
    letter-spacing: 1px;
    fill: var(--paper);
  }
  .event-title .live { fill: var(--signal); }
  .show-date {
    font-family: "Saira Condensed", sans-serif;
    font-weight: 600;
    font-size: 27px;
    fill: var(--paper);
  }
  .show-date .city { fill: var(--signal); }
  .dot-rule {
    stroke: var(--mustard);
    stroke-width: 2.4;
    stroke-linecap: round;
    stroke-dasharray: 0 7.5;
  }
  .presale {
    font-family: "Saira Condensed", sans-serif;
    font-weight: 400;
    font-size: 15px;
    fill: var(--mustard);
  }
</style>
</head>
<body>
<svg class="poster" viewBox="0 0 849 1200" width="849" height="1200" xmlns="http://www.w3.org/2000/svg">
  <defs>
    <linearGradient id="cover-tone" x1="0" y1="0" x2="0" y2="1">
      <stop offset="0" stop-color="#4A4A4D"/>
      <stop offset="0.6" stop-color="#55545A"/>
      <stop offset="1" stop-color="#6F7690"/>
    </linearGradient>
  </defs>

  <g class="microphone" transform="rotate(-10 497 732)">
    <!-- stand yoke -->
    <path class="mic-frame" d="M84 735 L100 1000 C115 1200 250 1335 505 1335 C705 1335 790 1200 790 1000 L790 830"/>
    <circle class="mic-knob" cx="84" cy="737" r="19"/>

    <!-- lower body -->
    <path class="mic-cup" d="M250 815 L772 815 L772 1000 C772 1205 660 1300 510 1300 C355 1300 250 1205 250 1000 Z"/>
    <path class="mic-rim" d="M726 850 L726 1000 C726 1180 640 1262 520 1268"/>

    <!-- podcast cover artwork -->
    <path role="img" aria-label="Podcast cover artwork: cartoon illustration of the two hosts, one in a black shirt and one giving a thumbs up in a light blue sweater, on a dark grey dotted backdrop"
          d="M238 650 L238 336 A260 260 0 0 1 758 336 L758 650 Z" fill="url(#cover-tone)"/>

    <!-- title band -->
    <rect class="mic-band" x="164" y="658" width="667" height="152" rx="76"/>
    <text class="event-title" x="512" y="758" text-anchor="middle">THE LANTERN TABLE - <tspan class="live">LIVE</tspan></text>

    <!-- show dates -->
    <line class="dot-rule" x1="320" y1="878" x2="660" y2="878"/>
    <text class="show-date" x="488" y="918" text-anchor="middle">Saturday, November 11, 2023 → <tspan class="city">Solothurn</tspan></text>
    <line class="dot-rule" x1="320" y1="946" x2="660" y2="946"/>
    <text class="show-date" x="492" y="987" text-anchor="middle">Wednesday, December 27, 2023 → <tspan class="city">Berne</tspan></text>
    <line class="dot-rule" x1="320" y1="1016" x2="660" y2="1016"/>
    <text class="show-date" x="494" y="1057" text-anchor="middle">Thursday, December 28, 2023 → <tspan class="city">Berne</tspan></text>
    <line class="dot-rule" x1="330" y1="1086" x2="660" y2="1086"/>

    <!-- presale -->
    <text class="presale" x="500" y="1130" text-anchor="middle">The Dome, information and tickets → www.kuppelfest.example</text>
  </g>
</svg>
</body>
</html>
```